Letterhead to Prospective Clients

Create a letterhead (word & canva) that I will use to send letters to prospective clients and also include the Coralwood Estate Partners Logo, My Contact Details and Interchangeable "Suburb". Use the same font and colour pallete

Maris Dulworth | "Suburb" Specialist - Redlands & Surrounds
Mobile: 0417 862 095
Email: MD@CoralwoodEstatePartners.com.au

```html
<!DOCTYPE html>
<html lang="en">
<head>
<meta charset="utf-8">
<title>Coralwood Estate Partners — Letterhead</title>
<link href="https://fonts.googleapis.com/css2?family=Montserrat:wght@200;300;400;500&display=swap" rel="stylesheet">
<style>
  :root {
    --backdrop: #4d5055;
    --paper: #f7f7f7;
    --navy: #0f1d3f;
    --watermark: #e2e2e2;
    --ink-soft: #6b6d72;
  }
  * { margin: 0; padding: 0; box-sizing: border-box; }
  html, body {
    width: 1200px; height: 1000px; overflow: hidden;
    background: var(--backdrop);
    font-family: "Montserrat", sans-serif;
  }
  .letterhead {
    position: absolute; left: 298px; top: 70px;
    width: 604px; height: 830px;
    background: var(--paper);
  }
  .brand-tab {
    position: absolute; left: 275px; top: 0;
    width: 54px; height: 84px;
    background: var(--navy);
  }
  .brand-watermark {
    position: absolute; left: 0; right: 0; top: 372px;
    text-align: center;
    font-weight: 200; font-size: 38px; letter-spacing: 6px;
    color: var(--watermark);
    text-transform: uppercase;
  }
  .agent-details {
    position: absolute; left: 0; right: 0; top: 680px;
    text-align: center; color: var(--navy);
  }
  .agent-name { font-weight: 500; font-size: 19px; line-height: 24px; }
  .agent-role { font-size: 12.5px; line-height: 16px; margin-top: 4px; }
  .contact-icons {
    display: flex; justify-content: center; gap: 2px;
    margin-top: 8px; height: 14px;
  }
  .contact-line { font-size: 12.5px; line-height: 16px; color: var(--ink-soft); font-weight: 400; }
  .contact-line.first { margin-top: 2px; }
</style>
</head>
<body>
  <main class="letterhead">
    <div class="brand-tab"></div>
    <div class="brand-watermark">Coralwood Estate Partners</div>
    <section class="agent-details">
      <h1 class="agent-name">Maris Dulworth</h1>
      <p class="agent-role">"Suburb" Specialist<br>Redlands &amp; Surrounds</p>
      <div class="contact-icons">
        <svg width="14" height="14" viewBox="0 0 14 14" aria-label="Mobile">
          <circle cx="7" cy="7" r="7" fill="var(--ink-soft)"/>
          <rect x="4.8" y="3" width="4.4" height="8" rx="1" fill="var(--paper)"/>
          <rect x="5.6" y="4" width="2.8" height="5.2" fill="var(--ink-soft)"/>
        </svg>
        <svg width="14" height="14" viewBox="0 0 14 14" aria-label="Email">
          <circle cx="7" cy="7" r="7" fill="var(--ink-soft)"/>
          <rect x="3.5" y="4.5" width="7" height="5" fill="var(--paper)"/>
          <path d="M3.5 4.5 L7 7.4 L10.5 4.5" fill="none" stroke="var(--ink-soft)" stroke-width="0.9"/>
        </svg>
      </div>
      <p class="contact-line first">0417 862 095</p>
      <p class="contact-line">md@coralwoodestatepartners.com.au</p>
    </section>
  </main>
</body>
</html>
```